(Wordpress)Website Design - No requirements! Sign Your name at the bottom of the site!

Dear Designer,

I am looking for a designer who is interested in a long-term business realtionship.
I already have 2 more designs to get done IMMEDIATELY after this website..
1.) An email brochure matching the website theme.
2.) A Billboard. BOTH MATCHING THE WEBSITE THEME

For this project, a bonus WILL be given.

Go to vaultnest.com as Site Inspiration

Please take this opportunity to design an existing wordpress website, FUNDSWIFTLANE.com, in whatever form your creativity takes you

I have no requirements other than a CREATIVE and OUT-OF -THE-BOX Design. Something Pretty and Eye Catching; a website that someone logs onto and doesnt want to leave

I have purchased a theme called velorant. You dont need to use it...But Info can be found at

http://skinbazaar.example/item/velorant-premium-wordpress-theme/full_screen_preview/482715

I have attached my logos and a PDF with a short story about what our company does.

Thank You,
-Tobin
PS I HAVE ANOTHER 2 DESIGNS TO DO AFTER THIS PROJECT.
also, IF YOU KNOW OF SOMEONE WHO DOES SEO WORK, I AM LOOKING FOR A FULL-TIME EMPLOYEE

Target Market(s)

Business Owners in a state of finacial NEED

Industry/Entity Type

Business

Requirements
Must have
• COLORFUL, EYE CATCHING

```html
<!DOCTYPE html>
<html lang="en">
<head>
<meta charset="utf-8">
<title>Swiftlane Funding</title>
<link rel="stylesheet" href="https://fonts.googleapis.com/css2?family=PT+Sans:wght@400;700&family=Archivo+Narrow:wght@700&family=Tinos:wght@400;700&family=Oswald:wght@500&display=swap">
<style>
:root{
  --page:#ffffff;
  --header:#f6f7f9;
  --sky:#00a2ef;
  --nav-top:#2a8fd0;
  --nav-bottom:#0d5d9c;
  --quote:#0b7fd0;
  --quote-mark:#8c9a5c;
  --text:#333333;
  --link:#1e7fe0;
  --form-bg:#efefef;
  --form-line:#d4d4d4;
  --blue-top:#4aa3df;
  --blue-bottom:#1669ad;
  --green-top:#84c431;
  --green-bottom:#4e9512;
  --lime:#d8f23a;
}
*{margin:0;padding:0;box-sizing:border-box}
html,body{width:922px;height:1200px;overflow:hidden;background:var(--page)}
body{position:relative;font-family:"Tinos",serif;color:var(--text)}
.abs{position:absolute}
.site-header{left:0;top:0;width:922px;height:112px;background:var(--header)}
.brand{left:18px;top:30px;display:flex;align-items:center;gap:10px}
.brand-dot{width:40px;height:40px;border-radius:50%;background:#1b6fb5}
.brand-name{font-family:"PT Sans",sans-serif;font-size:40px;color:#2a6fb8;letter-spacing:-1px}
.main-nav{left:483px;top:57px;width:426px;height:49px;background:linear-gradient(var(--nav-top),var(--nav-bottom));display:flex;font-family:"PT Sans",sans-serif;font-size:14px;color:#fff}
.main-nav span{display:flex;align-items:center;justify-content:center;height:100%;border-right:1px solid #3a8dc7;padding:0 16px}
.main-nav span:last-child{border:0;padding:0 16px 0 22px}
.nav-notch{left:520px;top:57px;width:0;height:0;border-left:8px solid transparent;border-right:8px solid transparent;border-top:10px solid var(--header)}
.sky-band{left:0;top:112px;width:922px;height:283px;background:var(--sky)}
.slider{left:30px;top:137px;width:842px;height:343px;background:#fff;box-shadow:0 18px 16px -12px rgba(0,0,0,.25)}
.slide-photo{left:3px;top:4px;width:457px;height:333px;background:linear-gradient(90deg,#d9d6d2 0%,#e9e8e6 60%,#ffffff 100%)}
.slide-quote{left:415px;top:95px;width:390px;font-family:"Archivo Narrow",sans-serif;font-size:23px;line-height:27px;color:var(--quote);text-align:justify}
.mark{font-family:"Oswald",sans-serif;font-size:44px;color:var(--quote-mark);line-height:1}
.mark-open{left:383px;top:72px}
.mark-close{left:580px;top:218px}
.dots{left:391px;top:509px;display:flex;gap:10px}
.dots i{width:16px;height:16px;border-radius:50%;background:radial-gradient(circle at 40% 35%,#e6e45a,#9a9a12);border:1px solid #8a8a20}
.dots i.on{background:radial-gradient(circle at 40% 35%,#a6c0ff,#2850c0);border-color:#2a4aa0}
.welcome-bar{left:8px;top:543px;width:630px;height:35px;background:linear-gradient(90deg,#f0f0f0,#f7f7f7 80%,#fff)}
.welcome{left:14px;top:562px;font-size:17px;color:#555}
.welcome b{font-weight:400;font-size:27px;color:var(--link);margin-left:4px}
.team-photo{left:8px;top:622px;width:290px;height:170px;background:linear-gradient(#f4f4f4,#4a4a4a 40%,#2e2e2e 80%,#f2f2f2)}
.intro{font-size:15px;line-height:22px}
.intro-a{left:305px;top:626px;width:340px}
.intro-b{left:14px;top:798px;width:620px}
.more-bar{left:8px;top:850px;width:630px;height:56px;background:linear-gradient(90deg,#f2f2f2,#f8f8f8 85%,#fff);box-shadow:0 4px 4px -2px rgba(0,0,0,.08)}
.read-more{left:14px;top:876px;font-size:15px;color:var(--link)}
.read-more span{letter-spacing:1px;margin-left:6px}
.promo{top:927px;width:310px;height:155px;border-radius:6px;color:#fff;font-family:"PT Sans",sans-serif}
.promo-download{left:10px;background:linear-gradient(var(--blue-top),var(--blue-bottom))}
.promo-call{left:336px;background:linear-gradient(var(--green-top),var(--green-bottom))}
.promo h2{font-family:"Archivo Narrow",sans-serif;font-size:25px;position:absolute;left:16px;top:6px;text-shadow:1px 1px 1px rgba(0,0,0,.4)}
.promo-copy{left:17px;top:36px;width:210px;font-size:11px;line-height:16px}
.promo-tag{left:17px;top:88px;font-size:11px;font-weight:700;font-style:italic;color:var(--lime)}
.dl-button{left:14px;top:110px;width:135px;height:36px;border-radius:18px;background:linear-gradient(#c8f2ff,#35b7e8);border:2px solid #0d6aa3;font-size:17px;color:#0b2c4a;display:flex;align-items:center;padding-left:20px;gap:6px}
.dl-button i{width:20px;height:20px;border-radius:50%;background:#1f2e3a;display:flex;align-items:center;justify-content:center}
.db-icon{left:246px;top:60px}
.call-lines{left:15px;top:48px;font-family:"Archivo Narrow",sans-serif;font-size:20px;line-height:26px;text-shadow:1px 1px 1px rgba(0,0,0,.3)}
.call-note{left:17px;top:114px;font-size:11px;font-style:italic;color:#111}
.apply{left:662px;top:552px;width:248px;height:521px;background:var(--form-bg);border:1px solid var(--form-line);border-radius:10px}
.apply h2{font-weight:400;font-size:22px;color:#222;padding:12px 0 10px 19px;border-bottom:1px solid var(--form-line)}
.field{position:absolute;left:19px}
.field label{display:block;font-size:15px;color:#222;margin-bottom:8px}
.field .input{width:209px;height:26px;background:#fff;border-top:2px solid #cfcfcf}
.field .select{width:137px;height:24px;background:#fff;border:1px solid #ccc;font-family:"PT Sans",sans-serif;font-size:10px;color:#666;display:flex;align-items:center;justify-content:space-between;padding:0 4px 0 7px}
.field .select i{width:14px;height:14px;background:#111;display:flex;align-items:center;justify-content:center}
.quote-btn{left:18px;top:476px;width:111px;height:27px;border-radius:3px;background:linear-gradient(#dff6ff,#5cc6f0);border:1px solid #2a8cc0;font-size:13px;font-weight:700;color:#15304a;display:flex;align-items:center;justify-content:center}
.footer-line{left:30px;top:1118px;width:880px;height:12px;background:linear-gradient(#fff,#e6e6e6);box-shadow:0 3px 4px -2px rgba(0,0,0,.15)}
.copyright{left:0;top:1153px;width:922px;text-align:center;font-family:"PT Sans",sans-serif;font-size:10px;color:#333}
</style>
</head>
<body>
<header class="abs site-header"></header>
<div class="abs brand"><span class="brand-dot"></span><span class="brand-name">SwiftlaneFunding</span></div>
<nav class="abs main-nav"><span>Application</span><span>Prequalified?</span><span>About Us</span><span>Swiftlane Charity</span></nav>
<div class="abs nav-notch"></div>

<div class="abs sky-band"></div>
<section class="abs slider">
  <div class="abs slide-photo" role="img" aria-label="Photo of a smiling business owner seated at a desk with a computer in a bright office"></div>
  <div class="abs mark mark-open">&ldquo;</div>
  <p class="abs slide-quote">I was having trouble finding working capital to invest into my business. With the banks making it ever more difficult to borrow money, I needed to think of something fast.</p>
  <div class="abs mark mark-close">&rdquo;</div>
</section>
<div class="abs dots"><i class="on"></i><i></i><i></i><i></i><i></i></div>

<div class="abs welcome-bar"></div>
<h1 class="abs welcome" style="font-weight:400">welcome to <b>Swiftlane Funding</b></h1>
<div class="abs team-photo" role="img" aria-label="Group photo of a business team in suits standing together"></div>
<p class="abs intro intro-a">Lorem ipsum dolor sit amet, consectetur adipiscing elit. Proin at nibh sapien. Curabitur nunc elit, tincidunt sed auctor id, posuere eget erat. Aliquam ac erat sed ante ornare scelerisque eu euismod velit. Curabitur nunc elit, tincidunt sed auctor id, posuere eget erat. Aliquam ac erat sed ante ornare scelerisque eu euismod velit.</p>
<p class="abs intro intro-b">Aliquam ac erat sed ante ornare scelerisque eu euismod velit. Curabitur nunc elit, tincidunt sed auctor id, posuere eget erat. Aliquam ac erat sed ante ornare scelerisque eu euismod velit.</p>
<div class="abs more-bar"></div>
<a class="abs read-more">Read More<span>····›</span></a>

<section class="abs promo promo-download">
  <h2>FREE Download</h2>
  <p class="abs promo-copy">As a client of Swiftlane Funding, you have free complimentary access to our Premier Client Lounge.</p>
  <p class="abs promo-tag">Premier Profitability Software &amp; Tools</p>
  <svg class="abs db-icon" width="48" height="56" viewBox="0 0 48 56">
    <ellipse cx="20" cy="8" rx="18" ry="6" fill="#e4e4e4"/>
    <rect x="2" y="8" width="36" height="38" fill="#c9c9c9"/>
    <ellipse cx="20" cy="46" rx="18" ry="6" fill="#b0b0b0"/>
    <path d="M2 21a18 6 0 0 0 36 0M2 33a18 6 0 0 0 36 0" stroke="#9a9a9a" fill="none"/>
    <path d="M30 28h10v12h7l-12 14-12-14h7z" fill="#5cc21e"/>
  </svg>
  <div class="abs dl-button">Download <i><svg width="10" height="10" viewBox="0 0 10 10"><path d="M3 1l4 4-4 4" stroke="#fff" stroke-width="2" fill="none"/></svg></i></div>
</section>

<section class="abs promo promo-call">
  <h2>Any Queries? Call Us</h2>
  <div class="abs call-lines">Toll Free: 888 555 0142<br>Fax: 888 555 0178</div>
  <p class="abs call-note">To send any mail please Click Here</p>
</section>

<aside class="abs apply">
  <h2>Apply Online</h2>
  <div class="field" style="top:58px"><label>Company Name</label><div class="input"></div></div>
  <div class="field" style="top:122px"><label>First Name</label><div class="input"></div></div>
  <div class="field" style="top:175px"><label>Last Name</label><div class="input"></div></div>
  <div class="field" style="top:232px"><label>Phone</label><div class="input"></div></div>
  <div class="field" style="top:288px"><label>Email</label><div class="input"></div></div>
  <div class="field" style="top:346px"><label>Business Age</label><div class="select">Under 6 Months<i><svg width="10" height="6"><path d="M0 0h10L5 6z" fill="#fff"/></svg></i></div></div>
  <div class="field" style="top:410px"><label>Monthly Credit Card Sales</label><div class="select">$0- $2,500<i><svg width="10" height="6"><path d="M0 0h10L5 6z" fill="#fff"/></svg></i></div></div>
  <div class="abs quote-btn">Get My Quote!</div>
</aside>

<div class="abs footer-line"></div>
<p class="abs copyright">© All Right Reserved, swiftlanefunding.com</p>
</body>
</html>
```